Folder and Swag Design for Law Firm

We are a personal injury law firm designing new client materials for folders and other swag that will go to clients once they retain us. Rather than just being white on green, or green on white, we'd like a design to put on the items. One idea that we had was a wave that included our slogan of "Our family protecting yours" that can wrap around a folder, or a tumbler but we are open to other ideas. I've attached a sketch of the wave design and our logo.
The final design should communicate a family protective feel.
Branding colors: #FFFFFF, #0FA57B, #00CA88
Victims of personal injury (car accidents, slip and falls, defective products).
Legal Services

```html
<!DOCTYPE html>
<html lang="en">
<head>
<meta charset="utf-8">
<title>Harlow &amp; Pierce — Client Folder</title>
<link rel="stylesheet" href="https://fonts.googleapis.com/css2?family=Cinzel:wght@400&family=Yellowtail&display=swap">
<style>
  :root {
    --page: #ffffff;
    --cover-green: #14ab8c;
    --pocket-teal: #0eb9a7;
    --band-green: #37a67c;
    --brand-green: #3aa67a;
    --slogan-green: #17a58a;
    --panel-white: #ffffff;
    --mark-faint-dark: #38b598;
    --mark-faint-light: #e5efea;
    --edge-shadow: rgba(0, 0, 0, 0.18);
  }
  html, body {
    margin: 0;
    padding: 0;
    width: 882px;
    height: 1200px;
    overflow: hidden;
    background: var(--page);
  }
  .folder-layout {
    display: block;
    width: 882px;
    height: 1200px;
  }
  .back-cover { fill: var(--cover-green); }
  .front-cover { fill: var(--panel-white); }
  .wave-white { fill: var(--panel-white); }
  .wave-band { fill: var(--band-green); }
  .pocket { fill: var(--pocket-teal); }
  .pocket-flap { fill: var(--pocket-teal); }
  .faint-mark--back { fill: var(--mark-faint-dark); }
  .faint-mark--front { fill: var(--mark-faint-light); }
  .brand-square { fill: var(--brand-green); }
  .firm-name {
    font-family: "Cinzel", "Times New Roman", serif;
    font-size: 27px;
    font-weight: 400;
    fill: var(--brand-green);
    letter-spacing: 1px;
  }
  .slogan {
    font-family: "Yellowtail", "Brush Script MT", cursive;
    font-size: 56px;
    fill: var(--slogan-green);
  }
</style>
</head>
<body>
<svg class="folder-layout" viewBox="246 906 1160 1578" xmlns="http://www.w3.org/2000/svg">
  <defs>
    <filter id="edge-shadow" x="-5%" y="-5%" width="110%" height="110%">
      <feDropShadow dx="2" dy="2" stdDeviation="2" flood-color="#000" flood-opacity="0.2"/>
    </filter>
  </defs>

  <g class="folder" filter="url(#edge-shadow)">
    <!-- covers -->
    <rect class="back-cover" x="320" y="1205" width="530" height="710"/>
    <rect class="front-cover" x="850" y="1205" width="530" height="710"/>

    <!-- faint brand squares -->
    <rect class="faint-mark--back" x="465" y="1427" width="221" height="183"/>
    <rect class="faint-mark--front" x="1013" y="1427" width="222" height="183"/>

    <!-- wave: white top line -->
    <path class="wave-white" d="M320 1678 C400 1725 480 1722 600 1700 C700 1682 790 1692 850 1700
      C950 1690 1040 1688 1150 1715 C1250 1738 1330 1725 1380 1688 L1380 1915 L320 1915 Z"/>
    <!-- wave: green band -->
    <path class="wave-band" d="M320 1690 C400 1735 480 1732 600 1712 C700 1696 790 1702 850 1708
      C950 1700 1040 1698 1150 1725 C1250 1748 1330 1735 1380 1700 L1380 1915 L320 1915 Z"/>
    <!-- wave: thin white line -->
    <path class="wave-white" d="M320 1730 C420 1748 520 1742 600 1726 C700 1708 790 1716 850 1722
      C950 1712 1040 1712 1150 1732 C1250 1752 1330 1748 1380 1735 L1380 1915 L320 1915 Z"/>
    <!-- pocket teal -->
    <path class="pocket" d="M320 1742 C420 1760 520 1754 600 1738 C700 1720 790 1728 850 1734
      C950 1724 1040 1724 1150 1744 C1250 1762 1330 1758 1380 1745 L1380 1915 L320 1915 Z"/>

    <!-- pocket flap -->
    <path class="pocket-flap" d="M320 1925 L290 1945 L273 1960 L273 2165 L300 2183 L540 2183
      C700 2180 798 2060 798 1915 L735 1915 L320 1925 Z"/>
  </g>

  <!-- firm identity -->
  <g class="firm-identity">
    <rect class="brand-square" x="914" y="1266" width="102" height="84"/>
    <text class="firm-name" x="1030" y="1315" textLength="312" lengthAdjust="spacingAndGlyphs">HARLOW &amp; PIERCE, LLC</text>
  </g>

  <!-- slogan -->
  <text class="slogan" x="888" y="1672" transform="rotate(4 888 1672)" textLength="455" lengthAdjust="spacingAndGlyphs">Our family protecting yours</text>
</svg>
</body>
</html>
```